Edit of flyers - text to be eddited

I currently have three flyers already designed, but want to edit the text on them. On the front of each flyer I want to delete the text which states: "50% off lawn mowing applies to first lawn mowed on any regular service and applies to first 100 callers so call now" and replace it with "Professional Lawn and Garden Maintenance".

Also on the front and rear of each flyer I want to replace the text which states "Tom and Marcus" with "Marcus Fellowes."

All other details can stay the same thanks. I need each of the files saved as a pdf according to the instructions attached with the bleed area set as specified for printing.

Font styles to use
Serif

Colors
acd036
fbed22

Requirements
Must have
• On the front of each flyer I want to delete the text which states: "50% off lawn mowing applies to first lawn mowed on any regular service and applies to first 100 callers so call now" and replace it with "Professional Lawn and Garden Maintenance".
• Also on the front and rear of each flyer I want to replace the text which states "Tom and Marcus" with "Marcus Fellowes."
• All other details can stay the same thanks. I need each of the files saved as a pdf according to the instructions attached with the bleed area set as specified for printing.

```html
<!DOCTYPE html>
<html lang="en">
<head>
<meta charset="utf-8">
<title>Greenway Lawns – Flyer Set</title>
<link rel="stylesheet" href="https://fonts.googleapis.com/css2?family=Lobster&family=Oswald:wght@500;700&family=Open+Sans:ital,wght@0,400;0,600;0,700;1,400;1,600&display=swap">
<style>
:root{
  --bg:#e9e9e9;
  --lime:#acd036;
  --yellow:#fbed22;
  --green:#1f8a3a;
  --green-dark:#146b2a;
  --green-mid:#3aa346;
  --red:#d7261e;
  --white:#ffffff;
  --ink:#2b2b2b;
}
*{box-sizing:border-box;margin:0;padding:0}
html,body{width:1200px;height:720px;overflow:hidden;background:var(--bg)}
body{position:relative;font-family:"Open Sans",sans-serif}
.card{position:absolute;overflow:hidden;box-shadow:0 2px 6px rgba(0,0,0,.25)}
.abs{position:absolute}
.script{font-family:"Lobster",cursive}
.cond{font-family:"Oswald",sans-serif}
.brand{font-family:"Oswald",sans-serif;font-weight:700;color:var(--green);white-space:nowrap;display:flex;align-items:center;gap:5px;justify-content:center}
.brand .dot{width:10px;height:10px;border-radius:50%;background:var(--lime);flex:none}

/* card 1 */
.promo{left:112px;top:32px;width:398px;height:204px;background:var(--white)}
.promo .offer{left:18px;top:24px;width:130px;color:var(--green);font-size:26px;line-height:.95;transform:rotate(-6deg)}
.promo .offer small{font-size:19px}
.promo .brand{left:8px;top:120px;width:145px;font-size:15px}
.promo .tag{left:6px;top:174px;width:150px;text-align:center;font-style:italic;font-size:8px;color:var(--green-dark);font-weight:600}
.promo .photo{left:162px;top:5px;width:230px;height:194px;background:linear-gradient(180deg,#f6b531 0%,#f8d85a 25%,#b9cf3c 45%,#7db52b 75%,#5d9a24 100%)}
.promo .banner{left:162px;top:90px;width:230px;height:24px;background:rgba(60,150,60,.85);color:var(--white);font-size:12px;line-height:24px;padding-left:24px;font-family:"Lobster",cursive;white-space:nowrap}
.promo .banner::before{content:"";position:absolute;left:4px;top:5px;border-left:11px solid var(--white);border-top:7px solid transparent;border-bottom:7px solid transparent}
.promo .contact{right:12px;bottom:10px;text-align:right;color:var(--white);font-size:7.5px;line-height:1.3}

/* card 2 */
.services-sign{left:668px;top:36px;width:396px;height:190px;background:linear-gradient(180deg,#3f8fd4 0%,#9cc9ef 35%,#cfe7b0 55%,#6fbd3c 75%,#3f9a2c 100%)}
.services-sign .intro{left:10px;top:10px;color:var(--white);font-size:11px;line-height:1.3}
.services-sign .name{right:10px;top:8px;text-align:right;color:var(--white)}
.services-sign .name .n{font-size:17px}
.services-sign .name .p{font-size:11px;color:var(--lime);font-weight:600}
.services-sign .name .w{font-size:11px;color:var(--white);font-weight:600}
.services-sign .posts{left:12px;top:52px;width:176px;height:136px;background:linear-gradient(180deg,rgba(70,160,70,.55),rgba(40,120,45,.7));border-radius:4px}
.services-sign ul{list-style:none;color:var(--white);font-size:8px;font-weight:600;line-height:15.5px;text-align:center;width:78px}
.services-sign .closing{right:10px;bottom:18px;width:230px;text-align:right;color:var(--white);font-size:11px;line-height:1.35}

/* card 3 */
.bold-band{left:100px;top:257px;width:420px;height:202px;background:linear-gradient(180deg,#4f8fd0 0%,#a6cde8 30%,#6fb33c 50%,#2f7a23 80%,#1c4f16 100%)}
.bold-band .head{left:0;top:0;width:100%;height:40px;background:var(--yellow);color:var(--red);font-size:21px;font-weight:700;text-align:center;line-height:40px;letter-spacing:-.3px}
.bold-band .left{left:13px;top:54px;color:var(--white);font-size:10px;font-style:italic;font-weight:600}
.bold-band .right{right:18px;top:52px;color:var(--white);font-size:10px;font-style:italic;font-weight:600}
.bold-band .brand{left:130px;top:100px;width:160px;height:40px;background:rgba(255,255,255,.9);border-radius:4px;font-size:17px}
.bold-band .who{left:40px;top:163px;color:var(--yellow);font-size:9px}
.bold-band .line{left:0;top:178px;width:100%;text-align:center;color:var(--yellow);font-size:12px;white-space:nowrap}

/* card 4 */
.grass-list{left:668px;top:260px;width:396px;height:190px;background:linear-gradient(180deg,#6fa8dd 0%,#b6d7ee 18%,#7cc04a 30%,#3c8a2a 55%,#1c2c12 80%,#111 100%)}
.grass-list .brand{left:133px;top:22px;width:130px;height:40px;background:rgba(255,255,255,.9);border-radius:4px;font-size:14px}
.grass-list .slogan{right:22px;top:14px;color:var(--white);font-size:11px;font-style:italic;font-weight:600}
.grass-list .ribbon{left:72px;top:96px;width:252px;height:13px;background:rgba(120,120,120,.7);color:var(--yellow);font-size:8.5px;line-height:13px;text-align:center;font-style:italic;font-weight:600;white-space:nowrap}
.grass-list ul{list-style:none;color:var(--white);font-size:6.8px;line-height:13px}
.grass-list li::before{content:"• "}
.grass-list .line{left:0;top:169px;width:100%;text-align:center;color:var(--yellow);font-size:11px;white-space:nowrap}

/* cards 5 & 6 */
.framed{width:416px;height:215px;background:var(--white)}
.framed .trim{position:absolute;background:#bbb}
.framed .inner{left:14px;top:16px;right:14px;bottom:16px;overflow:hidden}
.framed .bar{left:0;bottom:0;width:100%;height:40px;background:linear-gradient(180deg,#4aa33b,#1f7a2c);border-top:3px solid var(--yellow);display:flex;align-items:center;color:var(--white)}
.framed .bar .c1{width:120px;padding-left:20px;font-size:8px;line-height:1.15}
.framed .bar .c1 b{font-size:9px;font-weight:700}
.framed .bar .c1 i{font-size:4.5px;font-style:normal}
.framed .bar .c2{width:150px;border-left:1px solid var(--white);border-right:1px solid var(--white);text-align:center;font-size:11px}
.framed .bar .c3{flex:1;text-align:center;font-size:9px}

.scene{left:101px;top:478px}
.scene .view{left:0;top:0;width:100%;height:148px;background:linear-gradient(180deg,#5fa3dc 0%,#bfe0f4 35%,#d6ea9a 55%,#8fcb3d 80%,#5ea82a 100%)}
.scene .blossom{right:0;top:0;width:60px;height:120px;background:linear-gradient(200deg,#f3e6e8,rgba(243,230,232,0))}
.scene h1{left:0;top:10px;width:330px;text-align:center;color:var(--green);font-size:27px;line-height:1.2;font-weight:700;-webkit-text-stroke:.8px var(--white);paint-order:stroke fill}
.scene .brand{left:133px;top:115px;width:120px;font-size:12px}

.listed{left:658px;top:478px;width:417px}
.listed .view{left:0;top:0;width:100%;height:148px;background:linear-gradient(180deg,#dfe9f7 0%,#fafcff 50%,#eef6e3 80%,#8cc63f 100%)}
.listed .intro{left:20px;top:6px;font-size:7px;color:var(--ink)}
.listed ul{list-style:none;font-size:7px;font-weight:600;line-height:10px;color:var(--ink)}
.listed li::before{content:"";display:inline-block;width:5px;height:5px;background:var(--green-mid);transform:rotate(45deg);margin-right:4px}
.listed .note{left:20px;top:108px;font-size:6px;line-height:1.4;color:var(--ink)}
.listed .title{right:16px;top:14px;color:var(--green);font-size:25px;font-weight:700;-webkit-text-stroke:.8px var(--white);paint-order:stroke fill}
.listed .sub{right:20px;top:48px;font-size:7px;font-style:italic;color:var(--ink)}
.listed .garden{left:285px;top:62px;width:90px;height:80px;background:radial-gradient(ellipse at 60% 40%,rgba(248,197,28,.45),rgba(248,197,28,0) 70%)}
.listed .brand{left:150px;top:118px;width:120px;font-size:12px}
</style>
</head>
<body>

<section class="card promo">
  <div class="abs offer script">50% off<br><small>lawn mowing</small></div>
  <div class="abs brand"><span class="dot"></span>Greenway Lawns</div>
  <div class="abs tag">Lawn and Garden Maintenance</div>
  <div class="abs photo" role="img" aria-label="Sunlit meadow of yellow flowers under a glowing morning sky"></div>
  <div class="abs banner">Professional Lawn &amp; Garden Maintenance</div>
  <div class="abs contact">Marcus Fellowes<br>Ph: 0400555123<br>Email: greenwaylawns@mail.com<br>www.greenwaylawns.com.au</div>
</section>

<section class="card services-sign" role="img" aria-label="Open green field under a blue sky">
  <div class="abs intro script">At Greenway Lawns we specialise in<br>the following services:</div>
  <div class="abs name"><div class="n script">Marcus Fellowes</div><div class="p">Ph 0400555123</div><div class="w">www.greenwaylawns.com.au</div></div>
  <div class="abs posts" role="img" aria-label="Wooden signposts with green arrow signs naming each service"></div>
  <ul class="abs" style="left:18px;top:60px"><li>Lawn mowing</li><li>Edging</li><li>Blowing</li><li>Hedging</li><li>Pruning</li><li>Tree Loping</li><li>Weeding</li></ul>
  <ul class="abs" style="left:104px;top:60px"><li>Poisoning</li><li>Mulching</li><li>Fertilising</li><li>Rubbish removal</li><li>Planting</li><li style="font-size:6px">Lawn care and advice</li><li>Turf</li></ul>
  <div class="abs closing script">And any other garden maintenance job,<br>No job too big or too small.</div>
</section>

<section class="card bold-band" role="img" aria-label="Close-up of tall green grass blades against a blue sky">
  <div class="abs head cond">PROFESSIONAL LAWN &amp; GARDEN MAINTENANCE</div>
  <div class="abs left">Professional lawn mowing</div>
  <div class="abs right">at an affordable price</div>
  <div class="abs brand"><span class="dot"></span>Greenway Lawns</div>
  <div class="abs who cond">Marcus Fellowes</div>
  <div class="abs line cond">Ph: 0400555123 - Email: greenwaylawns@mail.com - www.greenwaylawns.com.au</div>
</section>

<section class="card grass-list" role="img" aria-label="Tall grass growing from dark soil under a blue sky">
  <div class="abs brand"><span class="dot"></span>Greenway Lawns</div>
  <div class="abs slogan">...No job too big or too small!</div>
  <div class="abs ribbon">At Greenway Lawns we specialise in the following services:</div>
  <ul class="abs" style="left:54px;top:113px"><li>Lawn mowing</li><li>Edging</li><li>Blowing</li><li>Hedging</li></ul>
  <ul class="abs" style="left:129px;top:113px"><li>Pruning</li><li>Tree Loping</li><li>Weeding</li><li>Poisoning</li></ul>
  <ul class="abs" style="left:196px;top:113px"><li>Mulching</li><li>Fertilising</li><li>Rubbish removal</li><li>Planting</li></ul>
  <ul class="abs" style="left:266px;top:113px"><li>Lawn care and advice</li><li>Turf</li></ul>
  <div class="abs" style="left:269px;top:140px;color:#fff;font-size:6.5px;font-style:italic;line-height:1.3">...and any other<br>garden maintenance job</div>
  <div class="abs line cond">Ph: 0400555123 - Email: greenwaylawns@mail.com - www.greenwaylawns.com.au</div>
</section>

<section class="card framed scene">
  <span class="trim" style="left:14px;top:0;width:1px;height:6px"></span>
  <span class="trim" style="right:14px;top:0;width:1px;height:6px"></span>
  <span class="trim" style="left:14px;bottom:0;width:1px;height:6px"></span>
  <span class="trim" style="right:14px;bottom:0;width:1px;height:6px"></span>
  <div class="abs inner">
    <div class="abs view" role="img" aria-label="Green rolling lawns with houses and a white picket fence under a bright sky"></div>
    <div class="abs blossom" role="img" aria-label="Pale pink blossom branch"></div>
    <h1 class="abs cond">Professional Lawn &amp;<br>Garden Maintenance</h1>
    <div class="abs brand"><span class="dot"></span>Greenway Lawns</div>
    <div class="abs bar cond">
      <div class="c1"><i style="font-size:5px">Marcus Fellowes</i><br><b>Ph: 0400555123</b><br><i>Email: greenwaylawns@mail.com</i></div>
      <div class="c2">Lawn &amp; Garden Maintenance</div>
      <div class="c3">www.greenwaylawns.com.au</div>
    </div>
  </div>
</section>

<section class="card framed listed">
  <span class="trim" style="left:14px;top:0;width:1px;height:6px"></span>
  <span class="trim" style="right:14px;top:0;width:1px;height:6px"></span>
  <span class="trim" style="left:14px;bottom:0;width:1px;height:6px"></span>
  <span class="trim" style="right:14px;bottom:0;width:1px;height:6px"></span>
  <div class="abs inner">
    <div class="abs view" role="img" aria-label="Soft pale sky fading into a strip of green grass"></div>
    <div class="abs intro">At Greenway Lawns we specialise in the following services:</div>
    <ul class="abs" style="left:22px;top:18px"><li>Lawn mowing</li><li>Blowing</li><li>Pruning</li><li>Weeding</li><li>Mulching</li><li>Rubbish removal</li><li>Lawn care and advice</li></ul>
    <ul class="abs" style="left:120px;top:18px"><li>Edging</li><li>Hedging</li><li>Tree Loping</li><li>Poisoning</li><li>Fertilising</li><li>Planting</li><li>Turf</li></ul>
    <div class="abs note">And any other garden maintenance job,<br>No job too big or too small.</div>
    <div class="abs title cond">Greenway Lawns</div>
    <div class="abs sub">Professional lawn mowing at an affordable price</div>
    <div class="abs garden" role="img" aria-label="Butterfly beside a yellow daisy on a stem"></div>
    <div class="abs brand"><span class="dot"></span>Greenway Lawns</div>
    <div class="abs bar cond">
      <div class="c1"><i style="font-size:5px">Marcus Fellowes</i><br><b>Ph: 0400555123</b><br><i>Email: greenwaylawns@mail.com</i></div>
      <div class="c2">Lawn &amp; Garden Maintenance</div>
      <div class="c3">www.greenwaylawns.com.au</div>
    </div>
  </div>
</section>

</body>
</html>
```